Book cover for "The Hollow Ledger"

Cover design measuring 42 x 29 cm + 2 cm trim margin for the non-fiction book "The Hollow Ledger." The content is about business model innovation in the furniture trade. The graphics should reference omnichannel, brick-and-mortar sales, and e-commerce in the furniture trade. The implementation should be playful, perhaps sketchy or abstract. Not conservative! The uploaded file should NOT be a design template. Rather, it should show the content that must be displayed on the cover. The final solution must be delivered in PDF format. The text must be editable.

```html
<!DOCTYPE html>
<html lang="en">
<head>
<meta charset="utf-8">
<title>The Hollow Ledger – Cover</title>
<link href="https://fonts.googleapis.com/css2?family=Cormorant+Garamond:wght@600&family=Source+Sans+3:wght@400&display=swap" rel="stylesheet">
<style>
  :root {
    --cream: #f5ecdc;
    --taupe: #a89c8c;
    --ink: #111111;
    --art-brick: #e2673a;
    --art-orange: #ee8a3a;
    --art-yellow: #f0c43c;
    --art-green: #5fa24c;
    --art-blue: #3f88c2;
    --art-sky: #8fc3df;
  }
  html, body {
    margin: 0;
    padding: 0;
    width: 1200px;
    height: 828px;
    overflow: hidden;
    background: var(--cream);
  }
  .cover {
    position: relative;
    width: 1200px;
    height: 828px;
    overflow: hidden;
    background: var(--cream);
  }
  .cover__waves {
    position: absolute;
    inset: 0;
    width: 1200px;
    height: 828px;
  }
  .cover__title {
    position: absolute;
    left: 590px;
    width: 552px;
    top: 128px;
    margin: 0;
    text-align: center;
    font-family: "Cormorant Garamond", "Times New Roman", serif;
    font-weight: 600;
    color: var(--ink);
    line-height: 1;
    text-shadow: 0 0 3px #fff, 0 0 3px #fff;
  }
  .cover__title-small {
    display: block;
    font-size: 56px;
    letter-spacing: 1px;
  }
  .cover__title-large {
    display: block;
    margin-top: 6px;
    font-size: 66px;
    letter-spacing: 0.5px;
    white-space: nowrap;
  }
  .cover__art {
    position: absolute;
    left: 626px;
    top: 378px;
    width: 474px;
    height: 240px;
    border-radius: 22px;
    background:
      radial-gradient(ellipse 90px 70px at 16% 32%, var(--art-brick) 0%, rgba(226,103,58,0.55) 55%, rgba(226,103,58,0) 100%),
      radial-gradient(ellipse 110px 80px at 84% 34%, var(--art-blue) 0%, rgba(63,136,194,0.5) 55%, rgba(63,136,194,0) 100%),
      radial-gradient(ellipse 80px 90px at 46% 72%, var(--art-green) 0%, rgba(95,162,76,0.5) 55%, rgba(95,162,76,0) 100%),
      radial-gradient(ellipse 90px 60px at 58% 58%, var(--art-yellow) 0%, rgba(240,196,60,0.5) 55%, rgba(240,196,60,0) 100%),
      linear-gradient(90deg, #f6c99a 0%, #f6dca6 45%, #cfe2ec 100%);
  }
  .cover__subtitle {
    position: absolute;
    left: 952px;
    top: 640px;
    margin: 0;
    font-family: "Source Sans 3", "Myriad Pro", sans-serif;
    font-weight: 400;
    font-size: 25px;
    line-height: 24.5px;
    color: var(--ink);
  }
</style>
</head>
<body>
  <main class="cover">
    <svg class="cover__waves" viewBox="0 0 2312 1596" preserveAspectRatio="none" aria-hidden="true">
      <defs>
        <linearGradient id="bandGlow" x1="0" y1="0" x2="1" y2="0">
          <stop offset="0" stop-color="#fdd699"/>
          <stop offset="0.35" stop-color="#fce5c0"/>
          <stop offset="0.7" stop-color="#fbe3b8"/>
          <stop offset="1" stop-color="#efe4d2"/>
        </linearGradient>
      </defs>
      <path d="M0 118 C300 130 600 260 850 420 C1000 510 1080 560 1140 600 L1000 560 C700 420 350 190 0 190 Z" fill="var(--taupe)"/>
      <path d="M0 190 C350 190 700 420 1000 560 C1200 640 1500 660 1800 560 C2050 470 2200 330 2312 250
               L2312 1420 C2000 1390 1700 1360 1400 1360 C1000 1370 500 1470 240 1596 L0 1596 Z" fill="url(#bandGlow)"/>
      <path d="M2312 110 C2230 190 2150 320 2100 400 L2140 400 C2200 330 2260 280 2312 250 Z" fill="var(--taupe)"/>
      <path d="M1380 1362 C1700 1360 2000 1400 2312 1420 L2312 1500 C2000 1470 1700 1410 1380 1362 Z" fill="var(--taupe)"/>
      <path d="M240 1596 C380 1530 520 1480 700 1440 C520 1500 400 1550 330 1596 Z" fill="var(--taupe)"/>
    </svg>

    <h1 class="cover__title">
      <span class="cover__title-small">THE</span>
      <span class="cover__title-large">HOLLOW LEDGER</span>
    </h1>

    <div class="cover__art" role="img" aria-label="Sketchy coloured illustration: a brick-and-mortar furniture shop and a computer screen showing an online armchair shop, joined by circular arrows around a person in an armchair using a laptop"></div>

    <p class="cover__subtitle">Business Model<br>Innovation in the<br>Furniture Trade</p>
  </main>
</body>
</html>
```